Roof wash and Gutter Cleaning

Would like to see our colors and logo incorporated into design along with phone number and before/after picture(s). We use a non pressure softwash process we use unlike high pressure. We are a exterior cleaning company that likes to set our standards high with safe methods to cleaning the everyday surfaces on homes.
“Serving the Tri-State Area”
A list of our services:
House washing
Shingle and metal roof washing
Deck cleaning
Window cleaning
Concrete cleaning
Gutter cleaning
415-362-0917
We do not need the address section as these will be more for our meet and greets. As well handed out as clipped door  postcards.

Target Market(s)
Shingle roof wash and gutter cleaning
Look and feel

```html
<!DOCTYPE html>
<html lang="en">
<head>
<meta charset="utf-8">
<title>Crestline Softwash Postcard</title>
<link href="https://fonts.googleapis.com/css2?family=Inter:wght@400;500;600;700&family=Poppins:ital,wght@0,600;1,600&family=Yellowtail&display=swap" rel="stylesheet">
<style>
  :root{
    --page:#a6a6a6;
    --white:#ffffff;
    --navy:#1d3557;
    --blue:#2a6db5;
    --blue-light:#5aa0dc;
    --blue-pale:#e8f1fa;
    --green:#5cb846;
    --text:#1f3350;
  }
  *{margin:0;padding:0;box-sizing:border-box}
  html,body{width:907px;height:1200px;overflow:hidden;background:var(--page)}
  body{position:relative;font-family:"Inter",sans-serif;color:var(--text)}
  .card{position:absolute;left:30px;width:847px;height:565px;background:var(--white);overflow:hidden}
  .card--front{top:28px}
  .card--back{top:608px}
  .card__art{position:absolute;inset:0}
  .brand{position:absolute;font-family:"Inter",sans-serif;font-weight:700;color:var(--blue)}
  .brand--front{left:44px;top:80px;font-size:44px;letter-spacing:-0.5px}
  .brand__sub{position:absolute;left:34px;top:180px;font-size:13px;font-weight:500;color:#6b7c93;font-style:normal}
  .kicker{position:absolute;left:0;width:847px;text-align:center;top:222px;font-weight:700;font-size:19px;letter-spacing:5px;color:var(--navy)}
  .headline{position:absolute;left:0;width:847px;text-align:center;top:250px;font-family:"Yellowtail",cursive;font-size:62px;color:var(--blue);line-height:1}
  .services{position:absolute;top:343px;list-style:none}
  .services--left{left:30px}
  .services--right{left:525px}
  .services li{display:flex;align-items:center;height:33px;font-size:25px;font-weight:500;color:var(--navy)}
  .services svg{width:26px;height:20px;margin-right:12px;flex:none}
  .tagline{position:absolute;left:57px;top:520px;font-family:"Poppins",sans-serif;font-style:italic;font-weight:600;font-size:19px;letter-spacing:1.2px;color:var(--white)}
  .contact{position:absolute;left:560px;top:458px;width:300px;text-align:center}
  .contact__icon{display:block;margin:0 auto 4px auto;width:30px;height:30px}
  .contact__label{font-size:10.5px;font-weight:500;color:var(--navy);letter-spacing:.3px}
  .contact__phone{font-family:"Poppins",sans-serif;font-weight:600;font-size:36px;color:var(--white);line-height:1.15}
  .segment{position:absolute;left:0;width:847px;text-align:center;top:36px;font-weight:600;font-size:16px;letter-spacing:3.5px;color:var(--white)}
  .title{position:absolute;left:0;width:847px;text-align:center;top:56px;font-weight:700;font-size:38px;color:var(--white)}
  .result{position:absolute;width:194px;height:135px}
  .result__tab{position:absolute;left:0;top:-11px;background:var(--white);border-radius:6px 6px 0 0;padding:3px 8px 0 8px;font-size:10.5px;font-weight:700;color:var(--navy);height:17px}
  .result__photo{width:100%;height:100%}
  .about{position:absolute;left:36px;top:492px;font-size:19.5px;line-height:24px;color:var(--navy)}
  .brand--back{right:38px;top:502px;font-size:28px}
</style>
</head>
<body>

<section class="card card--front">
  <svg class="card__art" width="847" height="565" viewBox="0 0 847 565">
    <defs>
      <linearGradient id="roofTone" x1="0" y1="0" x2="1" y2="1">
        <stop offset="0" stop-color="#2f4f2a"/>
        <stop offset=".3" stop-color="#7fb08a"/>
        <stop offset="1" stop-color="#6fc49a"/>
      </linearGradient>
      <linearGradient id="waveBlue" x1="0" y1="0" x2="1" y2="0">
        <stop offset="0" stop-color="#2a6db5"/>
        <stop offset=".6" stop-color="#5aa0dc"/>
        <stop offset="1" stop-color="#2a6db5"/>
      </linearGradient>
      <clipPath id="roofClip"><circle cx="830" cy="-20" r="280"/></clipPath>
    </defs>
    <path d="M0,330 C160,300 300,360 460,345 C620,330 720,300 847,310 L847,470 L0,470 Z" fill="#eef4fb"/>
    <g role="img" aria-label="Photo of a green metal roof half cleaned, trees behind">
      <rect x="540" y="-300" width="320" height="580" fill="url(#roofTone)" clip-path="url(#roofClip)"/>
    </g>
    <circle cx="830" cy="-20" r="280" fill="none" stroke="#2a6db5" stroke-width="8"/>
    <path d="M238,314 C350,306 520,306 630,302" stroke="#5cb846" stroke-width="4" fill="none" stroke-linecap="round"/>
    <path d="M0,448 C120,430 220,520 380,520 C480,520 520,500 580,470 C680,420 760,415 847,410 L847,565 L0,565 Z" fill="url(#waveBlue)"/>
  </svg>

  <div class="brand brand--front">Crestline</div>
  <p class="brand__sub">Exterior Cleaning &amp; Maintenance Co.</p>

  <p class="kicker">NON PRESSURE</p>
  <h1 class="headline">Softwash Cleaning</h1>

  <ul class="services services--left">
    <li><svg viewBox="0 0 26 20"><path d="M3,10 L10,17 L23,3" stroke="#5cb846" stroke-width="4" fill="none" stroke-linecap="round" stroke-linejoin="round"/></svg>House Washing</li>
    <li><svg viewBox="0 0 26 20"><path d="M3,10 L10,17 L23,3" stroke="#5cb846" stroke-width="4" fill="none" stroke-linecap="round" stroke-linejoin="round"/></svg>Shingle and Metal Roof Washing</li>
    <li><svg viewBox="0 0 26 20"><path d="M3,10 L10,17 L23,3" stroke="#5cb846" stroke-width="4" fill="none" stroke-linecap="round" stroke-linejoin="round"/></svg>Deck Cleaning</li>
  </ul>
  <ul class="services services--right">
    <li><svg viewBox="0 0 26 20"><path d="M3,10 L10,17 L23,3" stroke="#5cb846" stroke-width="4" fill="none" stroke-linecap="round" stroke-linejoin="round"/></svg>Window Cleaning</li>
    <li><svg viewBox="0 0 26 20"><path d="M3,10 L10,17 L23,3" stroke="#5cb846" stroke-width="4" fill="none" stroke-linecap="round" stroke-linejoin="round"/></svg>Concrete Cleaning</li>
    <li><svg viewBox="0 0 26 20"><path d="M3,10 L10,17 L23,3" stroke="#5cb846" stroke-width="4" fill="none" stroke-linecap="round" stroke-linejoin="round"/></svg>Gutter Cleaning</li>
  </ul>

  <p class="tagline">SERVING THE TRI-STATE AREA</p>

  <div class="contact">
    <svg class="contact__icon" viewBox="0 0 30 30">
      <circle cx="15" cy="15" r="15" fill="#5cb846"/>
      <path d="M10,8 L12.5,8 L13.5,11.5 L12,13 C13,15 15,17 17,18 L18.5,16.5 L22,17.5 L22,20 C22,21 21,22 20,22 C14,21.5 8.5,16 8,10 C8,9 9,8 10,8 Z" fill="#fff"/>
    </svg>
    <p class="contact__label">CONTACT US AT</p>
    <p class="contact__phone">415-362-0917</p>
  </div>
</section>

<section class="card card--back">
  <svg class="card__art" width="847" height="565" viewBox="0 0 847 565">
    <defs>
      <linearGradient id="headBlue" x1="0" y1="0" x2="1" y2="0">
        <stop offset="0" stop-color="#2a6db5"/>
        <stop offset=".5" stop-color="#4a8fd0"/>
        <stop offset="1" stop-color="#2a6db5"/>
      </linearGradient>
    </defs>
    <path d="M0,470 C200,440 400,480 600,450 C720,432 800,440 847,445 L847,565 L0,565 Z" fill="#eef4fb"/>
    <path d="M847,128 C700,160 600,150 480,138 C360,126 250,130 150,155 C90,170 40,185 0,200 L0,170 C40,155 90,140 150,125 C250,100 360,96 480,108 C600,120 700,130 847,110 Z" fill="#5cb846"/>
    <path d="M0,0 H847 V112 C700,132 600,122 480,110 C360,98 250,102 150,127 C90,142 40,157 0,172 Z" fill="url(#headBlue)" stroke="#fff" stroke-width="3"/>
  </svg>

  <p class="segment">RESIDENTIAL · COMMERCIAL</p>
  <h2 class="title">Exterior Cleaning &amp; Maintenance</h2>

  <figure class="result" style="left:28px;top:195px">
    <span class="result__tab">BEFORE</span>
    <svg class="result__photo" role="img" aria-label="Two-storey house with stained roof before washing"><defs><linearGradient id="h1" x1="0" y1="0" x2="0" y2="1"><stop offset="0" stop-color="#8a7d6e"/><stop offset=".5" stop-color="#d9cfa8"/><stop offset="1" stop-color="#4f5a3c"/></linearGradient></defs><rect width="100%" height="100%" fill="url(#h1)"/></svg>
  </figure>
  <figure class="result" style="left:226px;top:195px">
    <span class="result__tab">AFTER</span>
    <svg class="result__photo" role="img" aria-label="Same house with clean roof after softwash"><defs><linearGradient id="h2" x1="0" y1="0" x2="0" y2="1"><stop offset="0" stop-color="#9c8066"/><stop offset=".5" stop-color="#e3d8ad"/><stop offset="1" stop-color="#4f5a3c"/></linearGradient></defs><rect width="100%" height="100%" fill="url(#h2)"/></svg>
  </figure>
  <figure class="result" style="left:429px;top:195px">
    <span class="result__tab">BEFORE</span>
    <svg class="result__photo" role="img" aria-label="Gutter clogged with dry leaves"><defs><linearGradient id="g1" x1="0" y1="0" x2="1" y2="1"><stop offset="0" stop-color="#6b5440"/><stop offset="1" stop-color="#a48a6a"/></linearGradient></defs><rect width="100%" height="100%" fill="url(#g1)"/></svg>
  </figure>
  <figure class="result" style="left:626px;top:195px">
    <span class="result__tab">AFTER</span>
    <svg class="result__photo" role="img" aria-label="Clean empty gutter along a shingle roof"><defs><linearGradient id="g2" x1="0" y1="0" x2="1" y2="0"><stop offset="0" stop-color="#77777a"/><stop offset=".6" stop-color="#b9b9a8"/><stop offset="1" stop-color="#6a4a35"/></linearGradient></defs><rect width="100%" height="100%" fill="url(#g2)"/></svg>
  </figure>
  <figure class="result" style="left:28px;top:343px">
    <span class="result__tab">BEFORE</span>
    <svg class="result__photo" role="img" aria-label="Red shingle roof covered in debris"><defs><linearGradient id="r1" x1="0" y1="0" x2="1" y2="1"><stop offset="0" stop-color="#8e5a44"/><stop offset=".6" stop-color="#b49a82"/><stop offset="1" stop-color="#8a6650"/></linearGradient></defs><rect width="100%" height="100%" fill="url(#r1)"/></svg>
  </figure>
  <figure class="result" style="left:226px;top:343px">
    <span class="result__tab">AFTER</span>
    <svg class="result__photo" role="img" aria-label="Red shingle roof clean after washing"><defs><linearGradient id="r2" x1="0" y1="0" x2="1" y2="1"><stop offset="0" stop-color="#a35a42"/><stop offset=".7" stop-color="#b8715a"/><stop offset="1" stop-color="#c9c3bb"/></linearGradient></defs><rect width="100%" height="100%" fill="url(#r2)"/></svg>
  </figure>
  <figure class="result" style="left:429px;top:343px">
    <span class="result__tab">BEFORE</span>
    <svg class="result__photo" role="img" aria-label="Grey shingle roof with dark algae streaks"><defs><linearGradient id="s1" x1="0" y1="0" x2="0" y2="1"><stop offset="0" stop-color="#8a857c"/><stop offset="1" stop-color="#5d5a55"/></linearGradient></defs><rect width="100%" height="100%" fill="url(#s1)"/></svg>
  </figure>
  <figure class="result" style="left:626px;top:343px">
    <span class="result__tab">AFTER</span>
    <svg class="result__photo" role="img" aria-label="Same grey shingle roof cleaned"><defs><linearGradient id="s2" x1="0" y1="0" x2="0" y2="1"><stop offset="0" stop-color="#8f8a80"/><stop offset="1" stop-color="#7d7870"/></linearGradient></defs><rect width="100%" height="100%" fill="url(#s2)"/></svg>
  </figure>

  <p class="about">We are exterior cleaners that do everything from cleaning<br>your homes to your business fronts.</p>
  <div class="brand brand--back">Crestline</div>
</section>

</body>
</html>
```